Life Coach for Lawyers Business Card Design

Elegant, original, business card design for life coaching service for associate attorneys who work in big law and struggle with stress, overwhelm, and time management. Double sided design.

Target Market(s)

Women associate attorneys who work in big law and struggle with stress, overwhelm, and time management.

Industry/Entity Type

Life Coaching

Contact Information for Business Card

Marissa Pendrell
Life Coach
518.677.3941
calmbriefcounsel.net
marissa@calmbriefcounsel.net
@calmbriefcounsel (Instagram)

Font styles to use
Other font styles liked:
• Silver South font duo. See uploaded files.

Requirements
Must have
• Icons for phone, website, email, and Instagram instead of words. Specific colors used in my logo (171B2B, 421121, FFFFFF)
Nice to have
• Foil. Embossed. Feminine design.
Should not have
• Any colors other than those used in logo. See uploaded files.

```html
<!DOCTYPE html>
<html lang="en">
<head>
<meta charset="utf-8">
<title>Calm Brief Counsel – Business Card</title>
<link rel="stylesheet" href="https://fonts.googleapis.com/css2?family=Playfair+Display:wght@400;700;800&display=swap">
<style>
  :root {
    --backdrop: #c4c4d2;
    --burgundy-light: #6a0a10;
    --burgundy-dark: #3a0508;
    --foil: #d8ab8c;
    --paper: #e6e6e8;
    --ink: #2a0a10;
    --ink-soft: #3a2a2e;
  }
  * { box-sizing: border-box; margin: 0; padding: 0; }
  html, body {
    width: 1200px; height: 1200px; overflow: hidden;
    background: var(--backdrop);
    font-family: "Playfair Display", Georgia, serif;
  }
  .canvas { position: relative; width: 1200px; height: 1200px; }

  .card {
    position: absolute;
    width: 574px; height: 332px;
  }

  /* Front side */
  .card-front {
    left: 110px; top: 244px;
    background: linear-gradient(110deg, var(--burgundy-light) 0%, #520709 55%, var(--burgundy-dark) 100%);
  }
  .front-mark {
    position: absolute;
    left: 50%; top: 50%;
    transform: translate(-50%, -50%);
    width: 216px; height: 216px;
    border: 1.5px solid var(--foil);
    border-radius: 50%;
    display: flex; align-items: center; justify-content: center;
    text-align: center;
  }
  .front-name {
    color: var(--foil);
    font-weight: 400;
    font-size: 24px;
    line-height: 1.25;
    letter-spacing: 0.04em;
  }

  /* Back side */
  .card-back {
    left: 523px; top: 636px;
    background: var(--paper);
    color: var(--ink);
  }
  .holder { position: absolute; left: 66px; top: 46px; }
  .holder-name {
    font-weight: 800;
    font-size: 22px;
    letter-spacing: -0.01em;
    line-height: 1.1;
  }
  .holder-role {
    font-weight: 400;
    font-size: 13px;
    letter-spacing: 0.28em;
    margin-top: 3px;
    color: var(--ink-soft);
  }
  .contacts {
    position: absolute; left: 66px; top: 109px;
    list-style: none;
  }
  .contacts li {
    display: flex; align-items: center;
    height: 22.5px;
    font-size: 14px;
    color: var(--ink-soft);
  }
  .contacts svg {
    width: 13px; height: 13px;
    margin-right: 13px;
    flex: none;
  }
  .brand-name {
    position: absolute; right: 70px; bottom: 50px;
    font-weight: 400;
    font-size: 26px;
    letter-spacing: 0.02em;
    color: var(--ink);
  }
</style>
</head>
<body>
<main class="canvas">

  <section class="card card-front" aria-label="Card front">
    <div class="front-mark">
      <p class="front-name">Calm Brief<br>Counsel</p>
    </div>
  </section>

  <section class="card card-back" aria-label="Card back">
    <div class="holder">
      <h1 class="holder-name">Marissa Pendrell</h1>
      <p class="holder-role">LIFE COACH</p>
    </div>

    <ul class="contacts">
      <li>
        <svg viewBox="0 0 14 14" aria-hidden="true" fill="none" stroke="#2a0a10" stroke-width="1.6">
          <rect x="3.5" y="1" width="7" height="12" rx="1.2"/>
          <line x1="6" y1="11" x2="8" y2="11"/>
        </svg>
        518.677.3941
      </li>
      <li>
        <svg viewBox="0 0 14 14" aria-hidden="true" fill="none" stroke="#2a0a10" stroke-width="1.4">
          <path d="M1.5 5.5 L7 2 L12.5 5.5 V12 H1.5 Z"/>
          <path d="M1.5 5.5 L7 9 L12.5 5.5"/>
        </svg>
        marissa@calmbriefcounsel.net
      </li>
      <li>
        <svg viewBox="0 0 14 14" aria-hidden="true" fill="none" stroke="#2a0a10" stroke-width="1.5">
          <rect x="2" y="2" width="10" height="10" rx="2"/>
        </svg>
        calmbriefcounsel
      </li>
      <li>
        <svg viewBox="0 0 14 14" aria-hidden="true" fill="none" stroke="#2a0a10" stroke-width="1.2">
          <circle cx="7" cy="7" r="5.6"/>
          <ellipse cx="7" cy="7" rx="2.4" ry="5.6"/>
          <line x1="1.4" y1="7" x2="12.6" y2="7"/>
        </svg>
        calmbriefcounsel.net
      </li>
    </ul>

    <p class="brand-name">Calm Brief Counsel</p>
  </section>

</main>
</body>
</html>
```